Yacht Management in Miami & Ft Lauderdale (2019Q2)

I’m looking for a flyer to leave places for people to get information about my company and what services we offer.
We offer monthly management plans to ensure the vessel is ready to go at a moments notice. This can be as simple as washing once a week, or as involved as washing, waxing, detailing, provisioning, and crew services.
We also offer bespoke customizations; stereos, on board WiFi, and engineering.

Target Market(s)

Yacht and boat owners.

Font styles to use
Sans Serif

Colors
87d0c7
85cae6
85acd3
cedeed
cee9f5
cfeae6
0455a3

Requirements
Must have
• Must have simple attention grabbing, without being obnoxious.
• Prefer a 3in x 5in post card size. other size may be an option.
• Must be front and back.
Nice to have
• Languages: English, Spanish, Russian
• USA flag logo
Should not have
• Should not have a lot of text. Icons and photos are great.

```html
<!DOCTYPE html>
<html lang="en">
<head>
<meta charset="utf-8">
<title>Harbor Keepers – Yacht Management Flyer</title>
<link href="https://fonts.googleapis.com/css2?family=Nunito:wght@700;800;900&display=swap" rel="stylesheet">
<style>
  :root {
    --brand-blue: #1173bd;
    --deep-blue: #0f62ad;
    --panel-grey: #e6e7e8;
    --white: #ffffff;
    --photo-light: #e9cf9f;
    --photo-mid: #b48a5a;
    --photo-dark: #5d4632;
  }
  * { margin: 0; padding: 0; box-sizing: border-box; }
  html, body { width: 927px; height: 1200px; overflow: hidden; background: var(--white); }
  body { font-family: "Nunito", sans-serif; color: var(--deep-blue); }

  .flyer {
    position: relative;
    width: 927px; height: 1200px;
    background: var(--white);
  }
  .frame {
    position: absolute;
    left: 17px; top: 14px; width: 891px; height: 1166px;
    border: 15px solid var(--brand-blue);
  }
  .hero {
    position: absolute;
    left: 31px; top: 28px; width: 862px; height: 520px;
  }
  .brand {
    position: absolute;
    left: 92px; top: 200px;
    display: flex; align-items: center; gap: 14px;
    font-weight: 900; font-size: 46px; line-height: 1.05;
    color: var(--white); text-transform: uppercase; letter-spacing: 1px;
  }
  .brand-dot {
    width: 40px; height: 40px; border-radius: 50%;
    background: var(--white); flex: none;
  }
  .headline {
    position: absolute; left: 0; top: 549px; width: 927px;
    text-align: center; font-weight: 800; font-size: 30px;
    color: var(--deep-blue); letter-spacing: 0.2px;
  }
  .plans {
    position: absolute; left: 114px; top: 606px; width: 700px; height: 144px;
    background: var(--panel-grey);
  }
  .plans-icon { position: absolute; left: 14px; top: 14px; width: 110px; height: 112px; }
  .plans-title, .plans-promise {
    position: absolute; top: 23px;
    font-weight: 800; font-size: 20px; line-height: 26px; color: var(--brand-blue);
  }
  .plans-title { left: 128px; }
  .plans-promise { right: 30px; text-align: right; }

  .services {
    position: absolute; left: 113px; top: 766px; width: 701px;
    display: grid; grid-template-columns: repeat(3, 1fr);
    column-gap: 24px; row-gap: 20px;
  }
  .service {
    height: 141px; background: var(--brand-blue);
    display: flex; flex-direction: column; align-items: center; justify-content: flex-end;
    padding-bottom: 26px; color: var(--white);
  }
  .service svg { width: 64px; height: 64px; margin-bottom: 8px; }
  .service-name { font-weight: 800; font-size: 20px; }

  .contact {
    position: absolute; top: 1093px; left: 119px; width: 695px;
    display: flex; justify-content: space-between;
    font-weight: 800; font-size: 17px; line-height: 22px; color: var(--brand-blue);
  }
  .contact-right { text-align: right; }
</style>
</head>
<body>
<div class="flyer">
  <div class="frame"></div>

  <svg class="hero" viewBox="0 0 862 520" role="img" aria-label="Photo of a classic boat helm with wooden ship wheel and gauges, sunlit shoreline behind">
    <defs>
      <linearGradient id="heroTone" x1="0" y1="0" x2="1" y2="1">
        <stop offset="0" stop-color="var(--photo-dark)"/>
        <stop offset="0.35" stop-color="var(--photo-light)"/>
        <stop offset="0.7" stop-color="var(--photo-mid)"/>
        <stop offset="1" stop-color="var(--photo-dark)"/>
      </linearGradient>
    </defs>
    <path fill="url(#heroTone)" d="M0 0 H862 V490 C820 510 790 480 740 480 C690 480 660 510 610 505 C560 500 540 465 480 470 C420 475 400 510 340 505 C280 500 250 470 200 475 C150 480 120 505 70 500 C40 497 20 480 0 485 Z"/>
  </svg>

  <div class="brand"><span class="brand-dot"></span><span>Harbor<br>Keepers</span></div>

  <h1 class="headline">Yacht Management in Miami &amp; Ft Lauderdale</h1>

  <section class="plans">
    <svg class="plans-icon" viewBox="0 0 110 112" fill="none" stroke="var(--brand-blue)" stroke-width="4">
      <rect x="4" y="10" width="94" height="86" rx="4"/>
      <line x1="4" y1="26" x2="98" y2="26"/>
      <line x1="18" y1="4" x2="18" y2="16"/><line x1="30" y1="4" x2="30" y2="16"/>
      <line x1="72" y1="4" x2="72" y2="16"/><line x1="84" y1="4" x2="84" y2="16"/>
      <path d="M14 36 H88 V86 H14 Z M14 48 H88 M14 61 H88 M14 74 H88 M29 36 V86 M44 36 V86 M59 36 V86 M74 36 V86" stroke-width="3"/>
      <circle cx="86" cy="88" r="20" fill="var(--panel-grey)"/>
      <path d="M77 88 L84 95 L96 81"/>
    </svg>
    <p class="plans-title">Monthly<br>management<br>plans</p>
    <p class="plans-promise">We ensure<br>the vessel is ready<br>to go at a moments notice</p>
  </section>

  <section class="services">
    <div class="service">
      <svg viewBox="0 0 64 64" fill="none" stroke="var(--white)" stroke-width="3">
        <rect x="18" y="26" width="28" height="14"/>
        <path d="M22 40 V48 M28 40 V48 M34 40 V48 M40 40 V48"/>
        <rect x="6" y="50" width="52" height="6" fill="var(--white)"/>
        <circle cx="32" cy="12" r="2" fill="var(--white)"/><circle cx="20" cy="18" r="2" fill="var(--white)"/><circle cx="44" cy="18" r="2" fill="var(--white)"/>
      </svg>
      <span class="service-name">Washing</span>
    </div>
    <div class="service">
      <svg viewBox="0 0 64 64" fill="none" stroke="var(--white)" stroke-width="3">
        <path d="M10 36 H54 C54 50 44 58 32 58 C20 58 10 50 10 36 Z"/>
        <path d="M24 8 H56 V16 H32 V34"/>
        <path d="M24 8 V22 C24 26 30 26 30 22"/>
      </svg>
      <span class="service-name">Waxing</span>
    </div>
    <div class="service">
      <svg viewBox="0 0 64 64" fill="none" stroke="var(--white)" stroke-width="3">
        <circle cx="32" cy="32" r="20"/><circle cx="32" cy="32" r="12"/><circle cx="32" cy="32" r="4"/>
        <path d="M32 4 V60 M4 32 H60 M12 12 L52 52 M52 12 L12 52"/>
      </svg>
      <span class="service-name">Crew services</span>
    </div>
    <div class="service">
      <svg viewBox="0 0 64 64" fill="none" stroke="var(--white)" stroke-width="3">
        <rect x="4" y="8" width="18" height="48"/><rect x="42" y="8" width="18" height="48"/>
        <rect x="26" y="32" width="12" height="24"/>
        <circle cx="13" cy="20" r="4"/><circle cx="13" cy="40" r="7"/>
        <circle cx="51" cy="20" r="4"/><circle cx="51" cy="40" r="7"/>
      </svg>
      <span class="service-name">Stereos</span>
    </div>
    <div class="service">
      <svg viewBox="0 0 64 64" fill="none" stroke="var(--white)" stroke-width="5" stroke-linecap="round">
        <path d="M12 30 C24 18 40 18 52 30"/>
        <path d="M20 38 C27 31 37 31 44 38"/>
        <circle cx="32" cy="47" r="3" fill="var(--white)"/>
      </svg>
      <span class="service-name">On board WiFi</span>
    </div>
    <div class="service">
      <svg viewBox="0 0 64 64" fill="none" stroke="var(--white)" stroke-width="3">
        <circle cx="26" cy="26" r="20"/><circle cx="26" cy="26" r="9"/><circle cx="26" cy="26" r="3"/>
        <path d="M26 13 V17 M26 35 V39 M13 26 H17 M35 26 H39"/>
        <path d="M40 40 L58 58" stroke-width="5"/>
      </svg>
      <span class="service-name">Engineering</span>
    </div>
  </section>

  <footer class="contact">
    <p class="contact-left">4120 Bayline Court<br>Coral Bay, FL 33100</p>
    <p class="contact-right">(555) 014-2290<br>www.harborkeepers.example/hello@harborkeepers.example</p>
  </footer>
</div>
</body>
</html>
```